needing web design for aerial and satellite installation comapny

We need our website designing, it needs to be professional and look creative,
We are a aerial and satellite company called Kestrel Mend & Reach ()
I like this site design also some of the following maybe:

https://www.skywirelo.co.uk/

http://holdmoor.co.uk/

http://quillnine-guard.co.uk/portfolio/zmp-holdmoor/

The design will require coding once the design is complete, i haven't paid for this yet as i want to be sure the design is good before i commit.

The template needs to look professional and look like one of the leading companies.
The site will consist of all the features this site has https://www.skywirelo.co.uk/

I like a modern design with the latest technology.

Target Market(s)

tv aerial satellite installation

Industry/Entity Type

Satellite Tv

Number of Pages Required

3 page

Font styles to use
Sans Serif

Colors

Designer to choose colors to be used in the design.

Requirements
Must have
• eb Contest Brief We need our website designing, it needs to be professional and look creative,
• We are a aerial and satellite company called Kestrel Mend Reach ()
• I like this site design also some of the following maybe:
• https://www.skywirelo.co.uk/
• http://holdmoor.co.uk/
• http://quillnine-guard.co.uk/portfolio/zmp-holdmoor/
• The design will require coding once the design is complete, i haven't paid for this yet as i want to be sure the design is good before i commit.
• The template needs to look professional and look like one of the leading companies.
• The site will consist of all the features this site has https://www.skywirelo.co.uk/
• I like a modern design with the latest technology.
Nice to have
• http://holdmoor.co.uk/
Should not have
• poor design

```html
<!DOCTYPE html>
<html lang="en">
<head>
<meta charset="utf-8">
<title>Kestrel Mend &amp; Reach</title>
<link href="https://fonts.googleapis.com/css2?family=Oswald:wght@400;500;600&family=Open+Sans:wght@400;600;700&display=swap" rel="stylesheet">
<style>
:root{
  --orange:#f26a1b;
  --orange-dark:#d9560c;
  --ink:#333333;
  --muted:#777777;
  --line:#e3e3e3;
  --dark:#2b2f33;
  --darker:#1f2225;
  --paper:#ffffff;
  --soft:#f5f5f5;
}
*{box-sizing:border-box;margin:0;padding:0}
html,body{width:695px;height:1200px;overflow:hidden}
body{font-family:"Open Sans",Arial,sans-serif;color:var(--ink);background:var(--paper);font-size:6px;line-height:1.45}
h1,h2,h3,h4{font-family:"Oswald",Arial,sans-serif;font-weight:500}
.btn{display:inline-block;background:var(--orange);color:#fff;font-size:6px;font-weight:600;padding:4px 10px;border-radius:2px;line-height:1.2}

/* header */
.site-header{height:32px;display:flex;align-items:center;padding:0 28px;border-bottom:1px solid var(--line);overflow:hidden}
.brand{display:flex;align-items:center;gap:5px;width:130px}
.brand-mark{width:12px;height:12px;background:var(--dark)}
.brand-name{font-family:"Open Sans",sans-serif;font-weight:700;font-size:7px;color:var(--dark)}
.main-nav{display:flex;gap:14px;flex:1;font-size:6px;color:var(--ink)}
.main-nav .active{color:var(--orange)}
.header-contact{text-align:right;line-height:1.1}
.header-contact .label{font-size:5px;color:var(--muted)}
.header-contact .phone{font-family:"Oswald",sans-serif;font-size:11px;color:var(--orange);line-height:1.05}
.header-contact .btn{padding:2px 7px;font-size:5px;margin-top:1px}

/* hero */
.hero{position:relative;height:172px}
.hero-photo{position:absolute;inset:0;background:linear-gradient(100deg,#ece7e1 0%,#d9d2c9 45%,#bfb6aa 70%,#8f8a86 100%)}
.hero-box{position:absolute;left:40px;top:32px;width:222px;background:rgba(34,36,40,.86);padding:12px 14px;color:#fff}
.hero-box h1{font-size:24px;line-height:1.05;letter-spacing:.5px}
.hero-box h1 span{display:block;font-size:15px;color:#fff}
.hero-box p{font-size:5.5px;margin:7px 0 8px;color:#ddd}
.hero-dots{position:absolute;bottom:8px;left:50%;transform:translateX(-50%);display:flex;gap:4px}
.hero-dots i{width:5px;height:5px;border-radius:50%;background:#fff;opacity:.7}
.hero-dots i:first-child{background:var(--orange);opacity:1}

/* services */
.services{padding:18px 100px 0;text-align:center;height:276px}
.section-title{font-size:15px;color:var(--orange)}
.section-intro{font-size:5.5px;color:var(--muted);max-width:420px;margin:4px auto 10px}
.service-grid{display:grid;grid-template-columns:repeat(3,1fr);border-top:1px solid var(--line)}
.service-card{padding:9px 12px 10px;border-right:1px solid var(--line);border-bottom:1px solid var(--line)}
.service-card:nth-child(3n){border-right:none}
.service-card:nth-child(n+4){border-bottom:none}
.service-card svg{width:18px;height:18px;display:block;margin:0 auto 3px}
.service-card h3{font-size:8px;color:var(--orange)}
.service-card p{font-size:5px;color:var(--muted);margin:3px 0 6px}

/* contact band */
.contact-band{height:38px;background:var(--orange);display:flex;justify-content:center;gap:46px;align-items:center;color:#fff}
.contact-item{display:flex;align-items:center;gap:5px}
.contact-item .ic{width:15px;height:15px;border-radius:50%;background:#fff;display:flex;align-items:center;justify-content:center}
.contact-item small{display:block;font-size:5px;opacity:.9}
.contact-item strong{font-family:"Oswald",sans-serif;font-size:9px;font-weight:500}

/* how it works */
.how{position:relative;height:158px;padding:14px 28px 0}
.how h2{font-size:14px;color:var(--orange)}
.how .lead{font-size:5.5px;color:var(--muted);width:470px;margin:3px 0 10px}
.steps{display:grid;grid-template-columns:1fr 1fr;gap:10px 24px;width:300px;margin-left:40px}
.step{display:flex;gap:6px}
.step .num{flex:none;width:18px;height:18px;border:1px solid var(--line);border-radius:2px;display:flex;align-items:center;justify-content:center}
.step h4{font-size:7px;color:var(--ink)}
.step p{font-size:5px;color:var(--muted)}
.how-figure{position:absolute;right:40px;top:16px;width:120px;height:142px;background:linear-gradient(180deg,#cfdbe6 0%,#3f72b8 55%,#2b4f86 100%);border-radius:50% 50% 0 0/30% 30% 0 0}
.cta-strip{height:16px;display:flex;align-items:center;gap:8px;padding:0 28px;border-top:1px solid var(--line);border-bottom:1px solid var(--line);background:var(--soft)}
.cta-strip .btn{padding:2px 8px;font-size:5px}
.cta-strip p{font-size:5px;color:var(--muted);border-left:2px solid var(--orange);padding-left:5px}

/* testimonials */
.testimonials{height:122px;background:var(--orange);position:relative;text-align:center;color:#fff}
.testimonials .title-tab{display:inline-block;background:#fff;color:var(--ink);font-family:"Oswald",sans-serif;font-size:9px;padding:3px 22px}
.avatar{width:26px;height:26px;border-radius:50%;background:linear-gradient(135deg,#8a6d5c,#3d3430);margin:6px auto 2px;border:2px solid #fff}
.client-name{font-size:6px;font-weight:700}
.testimonials blockquote{font-size:5.5px;width:470px;margin:5px auto;line-height:1.6}
.testimonials .client-role{font-size:5px;opacity:.85}
.t-dots{display:flex;gap:4px;justify-content:center;margin-top:5px}
.t-dots i{width:4px;height:4px;border-radius:50%;background:#fff;opacity:.6}
.t-dots i:first-child{opacity:1}

/* blog */
.blog{height:182px;display:grid;grid-template-columns:repeat(3,1fr);gap:14px;padding:16px 140px 0}
.post-image{height:80px}
.post h4{font-size:7px;color:var(--orange);margin-top:5px}
.post .date{font-size:4.5px;color:var(--muted)}
.post p{font-size:5px;color:var(--muted);margin-top:2px}
.post .more{font-size:5px;color:var(--orange);display:block;text-align:right;margin-top:2px}

/* footer */
.site-footer{height:184px;background:var(--dark);color:#b7bcc1;padding:22px 140px 0;display:grid;grid-template-columns:1fr 1fr 0.9fr 1.1fr;gap:16px}
.site-footer h5{font-family:"Oswald",sans-serif;font-weight:500;font-size:7px;color:var(--orange);margin-bottom:6px}
.site-footer li{list-style:none;font-size:5px;margin-bottom:3px}
.site-footer li::before{content:"› ";color:var(--orange)}
.footer-brand{display:flex;flex-direction:column;align-items:center;gap:3px;margin-bottom:6px}
.footer-brand .brand-mark{background:#fff}
.footer-brand .brand-name{color:#fff;font-size:6px}
.site-footer p{font-size:5px}
.news-input{height:12px;background:#fff;border-radius:1px;margin:5px 0}
.site-footer .btn{padding:2px 8px;font-size:5px}
.copyright{height:20px;background:var(--darker);color:#8c9196;font-size:5px;display:flex;align-items:center;justify-content:center}
</style>
</head>
<body>

<header class="site-header">
  <div class="brand"><span class="brand-mark"></span><span class="brand-name">Kestrel Mend &amp; Reach</span></div>
  <nav class="main-nav">
    <span class="active">Home</span><span>Aerials</span><span>Satellite TV</span><span>Wall Mounting</span><span>Sound &amp; Home</span><span>Get a Quote</span><span>Contact Us</span>
  </nav>
  <div class="header-contact">
    <div class="label">Call Us Today</div>
    <div class="phone">800-5550-1427</div>
    <span class="btn">Book a Service</span>
  </div>
</header>

<section class="hero">
  <div class="hero-photo" role="img" aria-label="Smiling technician holding a remote beside a wall-mounted television in a bright living room"></div>
  <div class="hero-box">
    <h1>WELCOME TO<span>KESTREL MEND &amp; REACH</span></h1>
    <p>Trusted aerial and satellite installers covering homes and businesses, with same-day visits, fixed prices and a twelve month guarantee on every job.</p>
    <span class="btn">Get a Free Quote</span>
  </div>
  <div class="hero-dots"><i></i><i></i><i></i></div>
</section>

<section class="services">
  <h2 class="section-title">Our Services</h2>
  <p class="section-intro">From a single aerial repair to a full home entertainment setup, our engineers handle every job with care, clear pricing and tidy finishing.</p>
  <div class="service-grid">
    <article class="service-card">
      <svg viewBox="0 0 24 24" fill="none" stroke="#f26a1b" stroke-width="1.5"><path d="M12 22V8M4 6h16M6 10h12M8 14h8M12 8l-6-2M12 8l6-2"/></svg>
      <h3>TV Aerials</h3><p>New aerials, repairs and signal boosts for clear picture on every set.</p><span class="btn">Book a Service</span>
    </article>
    <article class="service-card">
      <svg viewBox="0 0 24 24" fill="none" stroke="#f26a1b" stroke-width="1.5"><path d="M5 17a9 9 0 0 1 9-12z"/><path d="M9 13l6-6M5 17l-2 4h8"/></svg>
      <h3>Satellite TV</h3><p>Dish fitting, alignment and multi-room feeds installed the same week.</p><span class="btn">Book a Service</span>
    </article>
    <article class="service-card">
      <svg viewBox="0 0 24 24" fill="none" stroke="#f26a1b" stroke-width="1.5"><rect x="6" y="3" width="12" height="18" rx="2"/><circle cx="12" cy="14" r="3.5"/><circle cx="12" cy="7" r="1.2"/></svg>
      <h3>Sound &amp; Home</h3><p>Soundbars and speakers set up and tuned to suit your living space.</p><span class="btn">Book a Service</span>
    </article>
    <article class="service-card">
      <svg viewBox="0 0 24 24" fill="none" stroke="#f26a1b" stroke-width="1.5"><path d="M3 11l9-7 9 7v9H3z"/><path d="M9 20v-6h6v6"/></svg>
      <h3>Smart Home Services</h3><p>Lighting, heating and door systems linked and ready from your phone.</p><span class="btn">Book a Service</span>
    </article>
    <article class="service-card">
      <svg viewBox="0 0 24 24" fill="none" stroke="#f26a1b" stroke-width="1.5"><path d="M2 9a15 15 0 0 1 20 0M5 13a10 10 0 0 1 14 0M8.5 16.5a5 5 0 0 1 7 0"/><circle cx="12" cy="20" r="1"/></svg>
      <h3>Wi-Fi Solutions</h3><p>Mesh networks and extenders for strong signal in every single room.</p><span class="btn">Book a Service</span>
    </article>
    <article class="service-card">
      <svg viewBox="0 0 24 24" fill="none" stroke="#f26a1b" stroke-width="1.5"><rect x="3" y="5" width="18" height="12" rx="1"/><path d="M8 21h8M12 17v4"/></svg>
      <h3>Commercial TV Systems</h3><p>Signal distribution for offices, hotels, pubs and large apartment blocks.</p><span class="btn">Book a Service</span>
    </article>
  </div>
</section>

<section class="contact-band">
  <div class="contact-item">
    <span class="ic"><svg width="8" height="8" viewBox="0 0 24 24" fill="#f26a1b"><path d="M6.6 10.8a15 15 0 0 0 6.6 6.6l2.2-2.2a1 1 0 0 1 1-.25 11.4 11.4 0 0 0 3.6.6 1 1 0 0 1 1 1V20a1 1 0 0 1-1 1A17 17 0 0 1 3 4a1 1 0 0 1 1-1h3.5a1 1 0 0 1 1 1c0 1.25.2 2.45.6 3.6a1 1 0 0 1-.25 1z"/></svg></span>
    <div><small>Free Phone</small><strong>0800 5550 1427</strong></div>
  </div>
  <div class="contact-item">
    <span class="ic"><svg width="8" height="8" viewBox="0 0 24 24" fill="#f26a1b"><path d="M6.6 10.8a15 15 0 0 0 6.6 6.6l2.2-2.2a1 1 0 0 1 1-.25 11.4 11.4 0 0 0 3.6.6 1 1 0 0 1 1 1V20a1 1 0 0 1-1 1A17 17 0 0 1 3 4a1 1 0 0 1 1-1h3.5a1 1 0 0 1 1 1c0 1.25.2 2.45.6 3.6a1 1 0 0 1-.25 1z"/></svg></span>
    <div><small>Local Office</small><strong>0121 555 0193</strong></div>
  </div>
  <div class="contact-item">
    <span class="ic"><svg width="8" height="8" viewBox="0 0 24 24" fill="none" stroke="#f26a1b" stroke-width="2.5"><rect x="3" y="5" width="18" height="14"/><path d="M3 5l9 8 9-8"/></svg></span>
    <div><small>Email Us</small><strong>hello@kestrelmend.co.uk</strong></div>
  </div>
</section>

<section class="how">
  <h2>How it Works</h2>
  <p class="lead">Getting your aerial or dish sorted takes four easy steps. Choose a service, get an instant price, pick a time that suits you and let our engineer handle the rest while you relax.</p>
  <div class="steps">
    <div class="step"><span class="num"><svg width="10" height="10" viewBox="0 0 24 24" fill="none" stroke="#f26a1b" stroke-width="2"><circle cx="11" cy="11" r="6"/><path d="M16 16l5 5"/></svg></span><div><h4>Browse Our Services</h4><p>See every job we cover and pick the one you need today.</p></div></div>
    <div class="step"><span class="num"><svg width="10" height="10" viewBox="0 0 24 24" fill="none" stroke="#f26a1b" stroke-width="2"><rect x="3" y="6" width="18" height="12"/><path d="M3 10h18"/></svg></span><div><h4>Get a Quote &amp; Pay</h4><p>Clear fixed prices with secure online payment options.</p></div></div>
    <div class="step"><span class="num"><svg width="10" height="10" viewBox="0 0 24 24" fill="none" stroke="#f26a1b" stroke-width="2"><rect x="3" y="5" width="18" height="16"/><path d="M3 10h18M8 3v4M16 3v4"/></svg></span><div><h4>Book a Visit</h4><p>Choose a date and time slot that fits around your day.</p></div></div>
    <div class="step"><span class="num"><svg width="10" height="10" viewBox="0 0 24 24" fill="none" stroke="#f26a1b" stroke-width="2.5"><path d="M4 12l5 5L20 6"/></svg></span><div><h4>Get Done</h4><p>Our engineer arrives, fits, tests and tidies up after.</p></div></div>
  </div>
  <div class="how-figure" role="img" aria-label="Engineer in a hard hat and blue overalls holding a tablet"></div>
</section>

<div class="cta-strip">
  <span class="btn">Book a Service</span>
  <p>Same-day appointments are often available. Call now or book online in under two minutes.</p>
</div>

<section class="testimonials">
  <h2 class="title-tab">What Client says</h2>
  <div class="avatar" role="img" aria-label="Client portrait"></div>
  <div class="client-name">Daniel Harwood</div>
  <blockquote>The engineer turned up on time, explained everything clearly and had our new aerial fitted within the hour. Picture quality is perfect on every channel now and the price was exactly what we were quoted online. I would happily recommend them to friends and family.</blockquote>
  <div class="client-role">Homeowner, Solihull</div>
  <div class="t-dots"><i></i><i></i><i></i></div>
</section>

<section class="blog">
  <article class="post">
    <div class="post-image" role="img" aria-label="Couple relaxing on a sofa watching television" style="background:linear-gradient(135deg,#d8d4cf,#8c8680)"></div>
    <h4>Sweet fresh stays of</h4><span class="date">Posted 12 March</span>
    <p>Simple tips to keep your TV signal strong through wind, rain and winter weather.</p><span class="more">Read More</span>
  </article>
  <article class="post">
    <div class="post-image" role="img" aria-label="Family gathered around a television in a living room" style="background:linear-gradient(135deg,#c9b9a4,#6d5f52)"></div>
    <h4>Ideas of rather leave,</h4><span class="date">Posted 28 February</span>
    <p>How to choose the right wall mount height for comfortable everyday viewing.</p><span class="more">Read More</span>
  </article>
  <article class="post">
    <div class="post-image" role="img" aria-label="Woman sitting on a sofa holding a remote control" style="background:linear-gradient(135deg,#d6c7b5,#a2693f)"></div>
    <h4>Sweet fresh stays of</h4><span class="date">Posted 9 February</span>
    <p>Satellite or aerial: a plain guide to picking the best option for your home.</p><span class="more">Read More</span>
  </article>
</section>

<footer class="site-footer">
  <div>
    <h5>Services</h5>
    <ul><li>TV Aerial Installation</li><li>Aerial Repairs</li><li>Satellite Dishes</li><li>TV Wall Mounting</li><li>Sound Systems</li><li>Smart Home Setup</li><li>Wi-Fi Solutions</li><li>Commercial Systems</li></ul>
  </div>
  <div>
    <h5>Popular Services</h5>
    <ul><li>Digital TV Upgrade</li><li>Multi-Room TV</li><li>Signal Boosting</li><li>Dish Alignment</li><li>Cable Management</li><li>Home Cinema Fitting</li><li>Business Signal Systems</li></ul>
  </div>
  <div>
    <h5>About Us</h5>
    <div class="footer-brand"><span class="brand-mark"></span><span class="brand-name">Kestrel Mend &amp; Reach</span></div>
    <p>Local aerial and satellite engineers with fixed prices, friendly service and a guarantee on every installation we complete.</p>
  </div>
  <div>
    <h5>Subscribe Newsletter</h5>
    <p>Get seasonal offers and handy signal tips sent to your inbox.</p>
    <div class="news-input"></div>
    <span class="btn">Subscribe</span>
  </div>
</footer>
<div class="copyright">© Kestrel Mend &amp; Reach. All Rights Reserved.</div>

</body>
</html>
```